QTM Website revamping

Make a website main page, navigation / menu options, couple of product pages in the 4 product categories, improvement on About us.
Our Website will need to be in PHP.
Our competitors websites for an idea.
www.norvask.com
https://frost.halbrook.com/en-gb/brands/tovrin
www.lumba.it
www.sarni.it
Our website is temporarily hosted at https://www.brightmarkweb.com/qtm/
Once done, we would like a quote for coding the entire website as well. If we find the quote good we will go ahead with you.

Target Market(s)

Industrial and Commercial Refrigeration , Cold Store, freezer and chiller manufacturers and commercial Airconditioning contractors and Industrial Automation panel makers.

Industry/Entity Type

Engineering

Number of Pages Required

5+ page

Font styles to use
Other font styles liked:
• "Michroma" "Roboto" "MONTSERRAT"

Colors
3377b5
ffffff

Requirements
Must have
• Main page, index/menu, couple of product pages.
Nice to have
• A good navigation to the product list
Font should be similar to the top menu line
Showcase our site as a good electronics temperature controller manufacturer for Refrigeration / Industrial Process Automation

```html
<!DOCTYPE html>
<html lang="en">
<head>
<meta charset="utf-8">
<title>QTM Controls – Home</title>
<link href="https://fonts.googleapis.com/css2?family=Montserrat:ital,wght@0,400;0,500;0,600;0,700;0,800;1,400&display=swap" rel="stylesheet">
<style>
:root{
  --blue:#3377b5;
  --blue-dark:#1f5a96;
  --red:#d92027;
  --green:#2e9a3f;
  --ink:#222;
  --muted:#777;
  --white:#fff;
  --footer:#2b2b2b;
  --footer-deep:#1e1e1e;
}
*{box-sizing:border-box;margin:0;padding:0}
html,body{width:1200px;height:3492px;overflow:hidden}
body{font-family:"Montserrat",sans-serif;color:var(--ink);background:var(--white);position:relative}
.abs{position:absolute}

/* header */
.site-header{position:absolute;left:0;top:0;width:1200px;height:102px;background:var(--white);border-top:3px solid var(--green)}
.brand{position:absolute;left:145px;top:12px;width:140px;height:84px;border:3px solid #333;border-radius:8px;display:flex;align-items:center;justify-content:center;font-weight:800;font-size:26px;color:var(--red);line-height:1;text-align:center}
.header-phone{position:absolute;right:144px;top:8px;display:flex;align-items:center;gap:12px;font-weight:600;font-size:24px;color:var(--blue)}
.main-nav{position:absolute;left:435px;top:68px;display:flex;gap:40px;font-size:14px;font-weight:500;color:#333}
.main-nav a{color:inherit;text-decoration:none;padding:2px 5px 12px;position:relative}
.main-nav a.active{border-bottom:3px solid var(--red)}

/* hero */
.hero{position:absolute;left:0;top:102px;width:1200px;height:598px;background:linear-gradient(180deg,#6d7176 0%,#9ea3a8 45%,#55595e 100%)}
.hero-title{position:absolute;left:0;width:1200px;text-align:center;font-weight:800;font-size:72px;letter-spacing:1px}
.hero-title.top{top:165px;color:var(--white)}
.hero-title.bottom{top:245px;color:var(--red)}
.hero-btn{position:absolute;left:498px;top:361px;width:204px;height:50px;border-radius:25px;background:var(--blue);color:var(--white);font-weight:600;font-size:16px;display:flex;align-items:center;justify-content:center;gap:8px}
.hero-dots{position:absolute;left:550px;top:520px;display:flex;gap:8px}
.hero-dots span{width:10px;height:10px;border-radius:50%;background:var(--white)}
.hero-dots span.on{background:var(--red)}
.hero-notch{position:absolute;left:560px;top:678px}

/* section titles */
.section-title{position:absolute;border:3px solid #222;display:flex;align-items:center;justify-content:center;font-weight:800;font-size:50px;letter-spacing:1px}
.section-title .r{color:var(--red)}
.section-title .g{color:var(--green);margin-left:14px}
.section-sub{position:absolute;left:0;top:922px;width:1200px;text-align:center;font-size:22px;color:#333}

/* product cards */
.product-card{position:absolute;top:1022px;width:290px;height:343px;background:var(--white);box-shadow:0 0 8px rgba(0,0,0,.12)}
.product-card .pic{position:absolute;left:14px;top:14px;width:262px;height:256px}
.product-card .label{position:absolute;left:0;bottom:0;width:290px;height:58px;color:var(--white);font-size:16px;font-weight:500;display:flex;align-items:center;padding-left:23px;clip-path:polygon(0 0,86% 0,100% 100%,0 100%)}
.label.blue{background:linear-gradient(90deg,#2f69a8,#3f85c6)}
.label.red{background:linear-gradient(90deg,#b8141b,#e02a30)}
.carousel-arrow{position:absolute;top:1171px;width:46px;height:46px;border:2px solid #555;border-radius:50%;display:flex;align-items:center;justify-content:center;background:var(--white)}

/* featured band */
.featured{position:absolute;left:0;top:1452px;width:1200px;height:365px;display:flex}
.featured-item{position:relative;width:400px;height:365px}
.featured-item .name{position:absolute;bottom:34px;left:0;width:100%;text-align:center;color:var(--white);font-weight:700;font-size:20px}
.f1{background:linear-gradient(160deg,#1c5a8c,#0f3d63)}
.f2{background:linear-gradient(160deg,#8fb3dc,#2a68a2)}
.f3{background:linear-gradient(160deg,#2a6aa3,#0e3a5f)}
.band-arrow{position:absolute;top:1600px}

/* news */
.news-card{position:absolute;top:2070px;width:279px;height:344px;background:var(--white);box-shadow:0 0 8px rgba(0,0,0,.1)}
.news-card .pic{width:100%;height:163px}
.news-card .body{padding:26px 19px 0;font-size:13px;font-weight:600;line-height:22px}
.news-card .date{margin-bottom:6px}
.news-card .badge{margin-top:12px;width:90px;height:44px;border-radius:6px;background:#e8eef6}

/* testimonials */
.testimonials{position:absolute;left:0;top:2514px;width:1200px;height:361px;background:var(--blue)}
.section-title.light{border-color:var(--white);color:var(--white)}
.quote-card{position:absolute;top:2781px;height:181px;background:var(--white);box-shadow:0 0 8px rgba(0,0,0,.15);text-align:center;padding:18px 34px 0}
.quote-card .mark{font-family:Georgia,serif;font-weight:700;font-size:64px;line-height:56px;color:var(--red);height:40px;overflow:hidden}
.quote-card p{font-style:italic;font-size:13px;line-height:22px;color:#888;margin-top:8px}
.quote-card::after{content:"";position:absolute;left:50%;bottom:-10px;margin-left:-10px;border:10px solid transparent;border-bottom:0;border-top-color:var(--white)}
.author{position:absolute;top:2976px;display:flex;align-items:center;gap:8px}
.author .avatar{width:44px;height:44px;border-radius:50%;background:#c9b7a3}
.author b{display:block;font-size:16px;color:#444}
.author small{font-size:10px;font-weight:600;color:#555}

/* footer */
.site-footer{position:absolute;left:0;top:3137px;width:1200px;height:277px;background:var(--footer);color:var(--white)}
.footer-notch{position:absolute;left:560px;top:3137px}
.footer-brand{position:absolute;left:145px;top:40px;width:140px;height:80px;background:var(--white);border-radius:6px;display:flex;align-items:center;justify-content:center;font-weight:800;font-size:26px;color:var(--red);text-align:center;line-height:1}
.socials{position:absolute;left:145px;top:160px;display:flex;gap:20px}
.socials span{width:26px;height:26px;border:2px solid var(--white);border-radius:4px}
.f-col{position:absolute;top:64px;font-size:12.5px;line-height:30px}
.f-col h4{font-weight:700;font-size:19px;line-height:22px;margin-bottom:8px}
.f-col .row{display:flex;align-items:center;gap:6px}
.bottom-bar{position:absolute;left:0;top:3414px;width:1200px;height:78px;background:var(--footer-deep);color:#ddd;font-size:11.5px;text-align:center;padding-top:40px}
</style>
</head>
<body>

<header class="site-header">
  <div class="brand">QTM Controls</div>
  <div class="header-phone">
    <svg width="38" height="38" viewBox="0 0 38 38"><circle cx="19" cy="19" r="17" fill="none" stroke="#d92027" stroke-width="2.5"/><path d="M13 11c1-1 2-1 3 0l2 3c.6 1 .3 1.8-.5 2.4l-1 .8c1 2 2.5 3.5 4.5 4.5l.8-1c.6-.8 1.4-1.1 2.4-.5l3 2c1 1 1 2 0 3l-1.5 1.5c-5 1-13-7-12-12z" fill="#d92027"/></svg>
    <span>91-20-41306728</span>
  </div>
  <nav class="main-nav">
    <a class="active">PRODUCTS</a><a>ABOUT US</a><a>RESOURCES</a><a>HIGHLIGHTS</a><a>CONTACT</a>
    <a><svg width="13" height="13" viewBox="0 0 13 13"><circle cx="5.5" cy="5.5" r="4" fill="none" stroke="#222" stroke-width="2"/><path d="M8.5 8.5l3.5 3.5" stroke="#222" stroke-width="2"/></svg></a>
  </nav>
</header>

<section class="hero" role="img" aria-label="Rooftop commercial refrigeration condensing units with steel ducting">
  <div class="hero-title top">COMMERCIAL</div>
  <div class="hero-title bottom">REFRIGERATION</div>
  <div class="hero-btn">GET STARTED
    <svg width="14" height="14" viewBox="0 0 14 14"><circle cx="7" cy="7" r="6.5" fill="#fff"/><path d="M6 4l3 3-3 3" stroke="#3377b5" stroke-width="2" fill="none"/></svg>
  </div>
  <div class="hero-dots"><span></span><span></span><span></span><span class="on"></span><span></span><span></span></div>
</section>
<svg class="hero-notch" width="80" height="22" viewBox="0 0 80 22"><path d="M0 22 L40 0 L80 22Z" fill="#fff"/><path d="M34 10l6 5 6-5" stroke="#999" stroke-width="1.5" fill="none"/></svg>

<div class="section-title" style="left:344px;top:777px;width:512px;height:100px"><span class="r">OUR</span><span class="g">PRODUCTS</span></div>
<p class="section-sub">The widest range of HVAC&amp;R and process control instrumentation.</p>

<div class="carousel-arrow" style="left:75px"><svg width="14" height="20" viewBox="0 0 14 20"><path d="M11 2L3 10l8 8" stroke="#444" stroke-width="2.5" fill="none"/></svg></div>
<div class="carousel-arrow" style="left:1078px"><svg width="14" height="20" viewBox="0 0 14 20"><path d="M3 2l8 8-8 8" stroke="#444" stroke-width="2.5" fill="none"/></svg></div>

<article class="product-card" style="left:144px">
  <div class="pic" role="img" aria-label="Round panel-mount temperature controller with red digital display" style="background:linear-gradient(180deg,#f4f4f4,#cfcfcf)"></div>
  <div class="label blue">HVAC&amp;R CONTROLLERS</div>
</article>
<article class="product-card" style="left:455px">
  <div class="pic" role="img" aria-label="Refrigeration electrical panel with digital display" style="background:linear-gradient(180deg,#f4f4f4,#d2d2d2)"></div>
  <div class="label red">HVACR ELECTRICAL PANELS</div>
</article>
<article class="product-card" style="left:766px">
  <div class="pic" role="img" aria-label="Industrial automation control panel with gauges" style="background:linear-gradient(180deg,#f4f4f4,#cccccc)"></div>
  <div class="label blue">INDUSTRIAL AUTOMATION</div>
</article>

<section class="featured">
  <div class="featured-item f1" role="img" aria-label="Compact controller with green digital readout">
    <div class="name">FROSTLINE</div>
  </div>
  <div class="featured-item f2" role="img" aria-label="Electrical panel unit with digital display">
    <div class="name">QRC-418300</div>
  </div>
  <div class="featured-item f3" role="img" aria-label="Industrial humidifier unit">
    <div class="name">HUMIDIFIER</div>
  </div>
</section>
<svg class="band-arrow" style="left:20px" width="34" height="64" viewBox="0 0 34 64"><path d="M30 2L4 32l26 30" stroke="rgba(255,255,255,.5)" stroke-width="2" fill="none"/></svg>
<svg class="band-arrow" style="left:1146px" width="34" height="64" viewBox="0 0 34 64"><path d="M4 2l26 30L4 62" stroke="rgba(255,255,255,.5)" stroke-width="2" fill="none"/></svg>

<div class="section-title" style="left:364px;top:1909px;width:472px;height:100px"><span class="r">LATEST</span><span class="g">NEWS</span></div>

<article class="news-card" style="left:155px">
  <div class="pic" role="img" aria-label="Night city skyline with connectivity signals" style="background:linear-gradient(180deg,#2a5290,#0d2148)"></div>
  <div class="body">
    <div class="date">25th to 27th February 2021</div>
    <div>SOUTHGATE TRADE HALLS, PUNE</div>
    <div class="badge"></div>
  </div>
</article>
<article class="news-card" style="left:461px">
  <div class="pic" role="img" aria-label="Abstract digital head with glowing light" style="background:linear-gradient(120deg,#0c2b6b,#2a6fd0 55%,#c98a4a)"></div>
  <div class="body">
    <div class="date">29th to 31st October 2020</div>
    <div>NORTHFIELD EXPO GROUNDS, JAIPUR</div>
    <div class="badge"></div>
  </div>
</article>
<article class="news-card" style="left:766px">
  <div class="pic" role="img" aria-label="Stainless steel cold room interior" style="background:linear-gradient(180deg,#e4e6e8,#9a9fa4)"></div>
  <div class="body">
    <div class="date">22nd to 25th September 2021</div>
    <div>HARBOUR EXPO HALL</div>
    <div>Visit us at : Stall No. I-20 to I-23</div>
    <div class="badge" style="margin-top:10px"></div>
  </div>
</article>

<section class="testimonials"></section>
<div class="section-title light" style="left:313px;top:2612px;width:574px;height:99px">OUR TESTIMONIALS</div>

<div class="quote-card" style="left:134px;width:302px"><div class="mark">&#8220;</div><p>In ullamcorper est eget tempor cursus neque mi consectetuer mi a ultricies massa est sed nisl Class aptent taciti sociosqu ad litora torquent per conubia nostra</p></div>
<div class="quote-card" style="left:449px;width:305px"><div class="mark">&#8220;</div><p>In ullamcorper est eget tempor cursus neque mi consectetuer mi a ultricies massa est sed nisl Class aptent taciti sociosqu ad litora torquent per conubia nostra</p></div>
<div class="quote-card" style="left:770px;width:296px"><div class="mark">&#8220;</div><p>In ullamcorper est eget tempor cursus neque mi consectetuer mi a ultricies massa est sed nisl Class aptent taciti sociosqu ad litora torquent per conubia nostra</p></div>

<div class="author" style="left:210px"><div class="avatar" role="img" aria-label="Client portrait"></div><div><b>By Author Name</b><small>City, Location</small></div></div>
<div class="author" style="left:522px"><div class="avatar" role="img" aria-label="Client portrait"></div><div><b>By Author Name</b><small>City, Location</small></div></div>
<div class="author" style="left:846px"><div class="avatar" role="img" aria-label="Client portrait"></div><div><b>By Author Name</b><small>City, Location</small></div></div>

<footer class="site-footer">
  <div class="footer-brand">QTM Controls</div>
  <div class="socials" aria-label="Social links"><span></span><span></span><span></span><span></span></div>

  <div class="f-col" style="left:397px">
    <h4>CONTACT US</h4>
    <div class="row"><svg width="9" height="12" viewBox="0 0 9 12"><path d="M4.5 0A4.5 4.5 0 0 0 0 4.5C0 8 4.5 12 4.5 12S9 8 9 4.5A4.5 4.5 0 0 0 4.5 0z" fill="#fff"/><circle cx="4.5" cy="4.5" r="1.6" fill="#2b2b2b"/></svg>B-42, Riverside Works Estate, Plot 7</div>
    <div>Lakeview Ring Road, Kothrud West</div>
    <div>Pune - 411 019, INDIA.</div>
    <div class="row"><svg width="11" height="11" viewBox="0 0 11 11"><path d="M2 0l2 3-1.2 1.2c.8 1.6 1.8 2.6 3.2 3.2L7.2 6l3 2-1 2.5C5 10.5.5 6 .3 1.5z" fill="#fff"/></svg>Phone : 0482 613 970</div>
    <div class="row"><svg width="12" height="9" viewBox="0 0 12 9"><rect width="12" height="9" rx="1" fill="#fff"/><path d="M0 1l6 4 6-4" stroke="#2b2b2b" fill="none"/></svg>Email : sales@qtmcontrols.com</div>
  </div>
  <div class="f-col" style="left:720px">
    <h4>QUICK LINKS</h4>
    <div>About Us</div><div>Products</div><div>Career</div><div>Contact</div><div>Gallery</div>
  </div>
  <div class="f-col" style="left:912px">
    <h4>OPENING HOURS</h4>
    <div>Monday - Saturday</div><div>7:00am to 5:00pm</div>
  </div>
</footer>
<svg class="footer-notch" width="80" height="22" viewBox="0 0 80 22"><path d="M0 0 L40 22 L80 0Z" fill="#fff"/><path d="M34 12l6-5 6 5" stroke="#999" stroke-width="1.5" fill="none"/></svg>
<div class="bottom-bar">© 2020 QTM Controls. All right reserved &nbsp;Term of Use &nbsp;| &nbsp;Privacy policy</div>

</body>
</html>
```